Design Business Card Aerial Drone Photography

we need a business card that shows we are a leader in:
-Aerial Videos
-Aerial Photography
-Aerial Real Estate Photography
the attached logo is in blue, however please feel free to submit creative colors and designs
Updates

I would like to add the words "Veteran Owned and Operated" to my business card Certified Drone Operator should appear as one line Thanks, Ray Colton

Target Market(s)

real estate, cell towers, companies that want to showcase their company with aerial drone photography

Contact Information for Business Card

logo files have been submitted in pdf, jpg, png, .ai, .eps., .svg formats. Please feel free to be creative with design and colors, possibly a cloud type background
sample attached.
review my website www.bluefinskyworks.com that should help with designing my business card
Services:
-Aerial Videos
-Aerial Photography

Font styles to use
Sans Serif

Colors

Designer to choose colors to be used in the design.

Requirements
Must have
• company logo
• Bluefin Sky Works
• Ray Colton Certified Drone Operator
• 770-519-8462
• bluefinskyworks@mailbox.example
• www.bluefinskywarks.com
• 2716 Marlow Ln, Larkfield GA 30412
Nice to have
• Please feel free to be creative with design and colors

```html
<!DOCTYPE html>
<html lang="en">
<head>
<meta charset="utf-8">
<title>Bluefin Sky Works – Business Card</title>
<link href="https://fonts.googleapis.com/css2?family=Arimo:wght@400;700&display=swap" rel="stylesheet">
<style>
  :root {
    --page-bg: #2b2b2d;
    --card-blue: #0b6fbf;
    --card-blue-deep: #075aa3;
    --card-dark: #2a2a2c;
    --logo-blue: #1677c9;
    --text-white: #ffffff;
    --text-ink: #0d1a2a;
    --text-grey: #d9d9d9;
    --sky-top: #3d8fdc;
    --sky-mid: #8cc0ef;
    --sky-light: #e6f2fc;
  }
  * { box-sizing: border-box; margin: 0; padding: 0; }
  html, body { width: 1200px; height: 997px; overflow: hidden; }
  body {
    background: var(--page-bg);
    font-family: "Arimo", Arial, sans-serif;
    position: relative;
  }
  .card {
    position: absolute;
    border-radius: 18px;
    overflow: hidden;
    box-shadow: 0 18px 40px rgba(0,0,0,0.55);
  }
  .card-back {
    left: 80px; top: 110px;
    width: 600px; height: 343px;
    background: radial-gradient(ellipse at 40% 15%, var(--sky-light) 0%, var(--sky-mid) 35%, var(--sky-top) 80%);
  }
  .card-front {
    left: 380px; top: 400px;
    width: 760px; height: 434px;
    background: var(--card-dark);
  }
  .front-blue {
    position: absolute;
    left: 0; top: 0; bottom: 0;
    width: 62%;
    background: linear-gradient(180deg, var(--card-blue) 0%, var(--card-blue-deep) 100%);
    clip-path: polygon(0 0, 74% 0, 100% 100%, 0 100%);
  }
  .front-contact {
    position: absolute;
    left: 0; top: 0; bottom: 0;
    width: 56%;
    padding: 52px 20px 40px 44px;
    display: flex;
    flex-direction: column;
  }
  .front-brand {
    position: absolute;
    right: 0; top: 0; bottom: 0;
    width: 46%;
    padding: 58px 36px 40px 40px;
    display: flex;
    flex-direction: column;
    justify-content: space-between;
  }
  .holder-name {
    color: var(--text-white);
    font-weight: 700;
    font-size: 19px;
    letter-spacing: 0.5px;
  }
  .holder-role {
    color: var(--text-ink);
    font-size: 14px;
    line-height: 1.45;
    margin-top: 6px;
  }
  .company-block { margin-top: 62px; }
  .company-name { color: var(--text-white); font-size: 17px; }
  .company-address { color: var(--text-ink); font-size: 14px; margin-top: 4px; }
  .contact-list {
    list-style: none;
    margin-top: auto;
  }
  .contact-list li {
    display: flex;
    align-items: center;
    gap: 12px;
    color: var(--text-ink);
    font-size: 15px;
    margin-top: 10px;
  }
  .contact-list svg { width: 20px; height: 20px; flex: none; }
  .brand-mark {
    display: flex;
    align-items: center;
    gap: 12px;
    justify-content: flex-end;
  }
  .brand-dot {
    width: 22px; height: 22px;
    border-radius: 50%;
    background: var(--logo-blue);
  }
  .brand-name {
    color: var(--logo-blue);
    font-weight: 700;
    font-size: 26px;
    letter-spacing: 0.5px;
  }
  .service-list {
    list-style: none;
    text-align: right;
    color: var(--text-grey);
    font-size: 14px;
    line-height: 1.6;
  }
</style>
</head>
<body>
  <div class="card card-back" role="img" aria-label="Bright blue sky with sun rays and white clouds behind the company emblem"></div>

  <div class="card card-front">
    <div class="front-blue"></div>
    <section class="front-contact">
      <h1 class="holder-name">RAY COLTON</h1>
      <p class="holder-role">Certified Drone Operator<br>Veteran Owned and Operated</p>

      <div class="company-block">
        <p class="company-name">Bluefin Sky Works</p>
        <p class="company-address">2716 Marlow Ln, Larkfield GA 30412</p>
      </div>

      <ul class="contact-list">
        <li>
          <svg viewBox="0 0 20 20" aria-hidden="true"><circle cx="10" cy="10" r="10" fill="#fff"/><path d="M7 5.5l1.6 0 .8 2.3-1 .9c.6 1.2 1.5 2.1 2.7 2.7l.9-1 2.3.8v1.6c0 .6-.5 1-1 1C9.6 13.6 6.4 10.4 6 6.5c0-.5.4-1 1-1z" fill="#0b6fbf"/></svg>
          770-519-8462
        </li>
        <li>
          <svg viewBox="0 0 20 20" aria-hidden="true"><circle cx="10" cy="10" r="10" fill="#fff"/><rect x="5" y="6.5" width="10" height="7" rx="1" fill="none" stroke="#0b6fbf" stroke-width="1.3"/><path d="M5.3 7l4.7 3.5L14.7 7" fill="none" stroke="#0b6fbf" stroke-width="1.3"/></svg>
          bluefinskyworks@mailbox.example
        </li>
        <li>
          <svg viewBox="0 0 20 20" aria-hidden="true"><circle cx="10" cy="10" r="10" fill="#fff"/><circle cx="10" cy="10" r="5" fill="none" stroke="#0b6fbf" stroke-width="1.2"/><ellipse cx="10" cy="10" rx="2.2" ry="5" fill="none" stroke="#0b6fbf" stroke-width="1.1"/><path d="M5 10h10" stroke="#0b6fbf" stroke-width="1.1"/></svg>
          www.bluefinskyworks.com
        </li>
      </ul>
    </section>

    <section class="front-brand">
      <div class="brand-mark">
        <span class="brand-dot"></span>
        <span class="brand-name">Bluefin Sky Works</span>
      </div>
      <ul class="service-list">
        <li>Aerial Videos</li>
        <li>Aerial Photography</li>
        <li>Aerial Real Estate Photography</li>
      </ul>
    </section>
  </div>
</body>
</html>
```